Content marketing firm needs a creative out of the box stationary design

Please take a look to the uploaded logo
I need the whole stationary package which include designs for (business card, letterhead, folder, notepad, company profile, small and big envelop, CD and its cover, key medal, header cover for social media pages "facebook, twitter, linkedin, insgram, google+" and website, favicon for website, E-mail signature, flyer, brochure)
Business

```html
<!DOCTYPE html>
<html lang="en">
<head>
<meta charset="utf-8">
<title>Gemline Media — Stationery Set</title>
<link href="https://fonts.googleapis.com/css2?family=Open+Sans:wght@400;600;800&display=swap" rel="stylesheet">
<style>
  :root {
    --backdrop: #5f6170;
    --brand-blue: #2ea7df;
    --brand-blue-deep: #249ed6;
    --paper: #ffffff;
    --paper-shade: #f1f1f1;
    --ink: #1c1c1c;
    --faint-blue: rgba(255, 255, 255, 0.12);
    --faint-grey: rgba(0, 0, 0, 0.07);
    --flap-line-blue: rgba(0, 70, 120, 0.18);
    --flap-line-white: rgba(0, 0, 0, 0.09);
  }
  * { box-sizing: border-box; margin: 0; padding: 0; }
  html, body { width: 788px; height: 1200px; overflow: hidden; }
  body {
    position: relative;
    background: var(--backdrop);
    font-family: "Open Sans", Arial, sans-serif;
  }
  .piece {
    position: absolute;
    overflow: hidden;
    box-shadow: 4px 6px 10px rgba(0, 0, 0, 0.28);
  }
  .piece--blue { background: linear-gradient(180deg, #33ade3, var(--brand-blue-deep)); color: var(--ink); }
  .piece--white { background: linear-gradient(180deg, var(--paper), var(--paper-shade)); color: var(--ink); }

  .business-card { width: 256px; height: 122px; left: 131px; }
  .business-card--blue { top: 89px; }
  .business-card--white { top: 237px; height: 119px; }
  .envelope-small { width: 247px; left: 432px; }
  .envelope-small--blue { top: 89px; height: 122px; }
  .envelope-small--white { top: 237px; height: 119px; }
  .letterhead { width: 247px; height: 349px; left: 127px; }
  .letterhead--white { top: 387px; }
  .letterhead--blue { top: 766px; height: 348px; }
  .envelope-large { width: 247px; height: 349px; left: 432px; }
  .envelope-large--white { top: 387px; }
  .envelope-large--blue { top: 766px; height: 348px; }

  .flap { position: absolute; left: 0; top: 0; width: 100%; height: 60px; }

  .diamond-art {
    position: absolute;
    border-radius: 40% 40% 50% 50%;
  }
  .piece--blue .diamond-art { background: radial-gradient(ellipse at center, var(--faint-blue), rgba(255,255,255,0.03) 70%); }
  .piece--white .diamond-art { background: radial-gradient(ellipse at center, var(--faint-grey), rgba(0,0,0,0.01) 70%); }
  .business-card .diamond-art { left: 140px; top: 6px; width: 100px; height: 92px; }
  .letterhead .diamond-art { left: 80px; top: 150px; width: 190px; height: 175px; }

  .brand {
    display: flex;
    align-items: center;
    gap: 4px;
    font-weight: 800;
    color: var(--ink);
    white-space: nowrap;
  }
  .brand__mark { background: var(--ink); }
  .business-card .brand { position: absolute; left: 12px; top: 16px; font-size: 7px; }
  .business-card .brand__mark { width: 7px; height: 7px; }
  .letterhead .brand { position: absolute; left: 0; right: 0; top: 100px; justify-content: center; font-size: 13px; }
  .letterhead .brand__mark { width: 12px; height: 12px; }

  .card-address { position: absolute; left: 56px; top: 20px; font-size: 4px; color: rgba(0,0,0,0.7); }

  .contact-list { position: absolute; list-style: none; font-weight: 600; }
  .contact-list li { display: flex; align-items: center; gap: 4px; }
  .business-card .contact-list { left: 12px; top: 64px; font-size: 4px; }
  .business-card .contact-list li { height: 9px; }
  .letterhead .contact-list { left: 10px; bottom: 10px; font-size: 5px; }
  .letterhead .contact-list li { height: 10.5px; }
  .contact-list svg { width: 6px; height: 6px; flex: none; }
  .letterhead--blue .contact-list svg { display: none; }
  .letterhead--blue .contact-list { left: 17px; bottom: 8px; }
</style>
</head>
<body>

  <!-- Business card, blue -->
  <section class="piece piece--blue business-card business-card--blue">
    <div class="diamond-art" role="img" aria-label="Faint sketched diamond illustration"></div>
    <div class="brand"><span class="brand__mark"></span>Gemline Media</div>
    <p class="card-address">14 Harbour Lane, Riverton 2040</p>
    <ul class="contact-list">
      <li><svg viewBox="0 0 6 6"><rect x="0.5" y="1" width="5" height="4" fill="none" stroke="#1c1c1c" stroke-width="0.8"/></svg>000 00 00 00</li>
      <li><svg viewBox="0 0 6 6"><path d="M1 1 L2.3 1 L2.8 2.4 L2 3 Q3 4.3 3.2 4 L3.6 3.3 L5 3.8 L5 5 Q2 5 1 1 Z" fill="#1c1c1c"/></svg>000 00 00 00</li>
      <li><svg viewBox="0 0 6 6"><circle cx="3" cy="3" r="2.4" fill="none" stroke="#1c1c1c" stroke-width="0.8"/></svg>www.company.com</li>
      <li><svg viewBox="0 0 6 6"><rect x="0.5" y="1.2" width="5" height="3.6" fill="#1c1c1c"/></svg>yourcompany@email.com</li>
    </ul>
  </section>

  <!-- Small envelope, blue -->
  <section class="piece piece--blue envelope-small envelope-small--blue">
    <svg class="flap" viewBox="0 0 247 60" preserveAspectRatio="none"><polyline points="0,0 22,53 247,53" fill="none" stroke="var(--flap-line-blue)" stroke-width="1"/></svg>
  </section>

  <!-- Business card, white -->
  <section class="piece piece--white business-card business-card--white">
    <div class="diamond-art" role="img" aria-label="Faint sketched diamond illustration"></div>
    <div class="brand"><span class="brand__mark"></span>Gemline Media</div>
    <p class="card-address">14 Harbour Lane, Riverton 2040</p>
    <ul class="contact-list">
      <li><svg viewBox="0 0 6 6"><circle cx="3" cy="3" r="2.6" fill="var(--brand-blue)"/></svg>000 00 00 00</li>
      <li><svg viewBox="0 0 6 6"><circle cx="3" cy="3" r="2.6" fill="var(--brand-blue)"/></svg>000 00 00 00</li>
      <li><svg viewBox="0 0 6 6"><circle cx="3" cy="3" r="2.6" fill="var(--brand-blue)"/></svg>www.company.com</li>
      <li><svg viewBox="0 0 6 6"><circle cx="3" cy="3" r="2.6" fill="var(--brand-blue)"/></svg>yourcompany@email.com</li>
    </ul>
  </section>

  <!-- Small envelope, white -->
  <section class="piece piece--white envelope-small envelope-small--white">
    <svg class="flap" viewBox="0 0 247 60" preserveAspectRatio="none"><polyline points="0,0 22,50 247,50" fill="none" stroke="var(--flap-line-white)" stroke-width="1"/></svg>
  </section>

  <!-- Letterhead, white -->
  <section class="piece piece--white letterhead letterhead--white">
    <div class="diamond-art" role="img" aria-label="Large faint sketched diamond illustration"></div>
    <div class="brand"><span class="brand__mark"></span>Gemline Media</div>
    <ul class="contact-list">
      <li><svg viewBox="0 0 6 6"><circle cx="3" cy="3" r="2.6" fill="var(--brand-blue)"/></svg>000 00 00 00</li>
      <li><svg viewBox="0 0 6 6"><circle cx="3" cy="3" r="2.6" fill="var(--brand-blue)"/></svg>000 00 00 00</li>
      <li><svg viewBox="0 0 6 6"><circle cx="3" cy="3" r="2.6" fill="var(--brand-blue)"/></svg>www.company.com</li>
      <li><svg viewBox="0 0 6 6"><circle cx="3" cy="3" r="2.6" fill="var(--brand-blue)"/></svg>yourcompany@email.com</li>
    </ul>
  </section>

  <!-- Large envelope, white -->
  <section class="piece piece--white envelope-large envelope-large--white">
    <svg class="flap" viewBox="0 0 247 60" preserveAspectRatio="none"><polyline points="4,0 22,52 272,52 247,0" fill="none" stroke="var(--flap-line-white)" stroke-width="1"/></svg>
  </section>

  <!-- Letterhead, blue -->
  <section class="piece piece--blue letterhead letterhead--blue">
    <div class="diamond-art" role="img" aria-label="Large faint sketched diamond illustration"></div>
    <div class="brand"><span class="brand__mark"></span>Gemline Media</div>
    <ul class="contact-list">
      <li><svg viewBox="0 0 6 6"></svg>000 00 00 00</li>
      <li><svg viewBox="0 0 6 6"></svg>000 00 00 00</li>
      <li><svg viewBox="0 0 6 6"></svg>www.company.com</li>
      <li><svg viewBox="0 0 6 6"></svg>yourcompany@email.com</li>
    </ul>
  </section>

  <!-- Large envelope, blue -->
  <section class="piece piece--blue envelope-large envelope-large--blue">
    <svg class="flap" viewBox="0 0 247 60" preserveAspectRatio="none"><polyline points="4,0 22,53 247,53" fill="none" stroke="var(--flap-line-blue)" stroke-width="1"/></svg>
  </section>

</body>
</html>
```